Fuel Your Day: Designing Eye-Catching Energy Ball Packaging

Here are the task requirements for my new project ENERGY BALLS under my existing baking business, Velvet_Crumb_by_Nora
Looking to create standout packaging that aligns with my brands fun and vibrant identity while allowing room for future growth and product line expansion.
1. Develop 3 Different Packaging Designs:
Create unique packaging for three different energy ball flavors to be launched initially.
2. Flexible Design for Future Modifications:
Ensure the packaging design is adaptable to accommodate new flavors or variations in the future. The initial 3 flavors are:
(i) Dates, Cashew & Chocolate
(ii) Dates, Cranberries & Oatmeal
(iii) Dates, Cashew & Ginger
3. Distinct Color Scheme for Each Flavor:
Use live and vibrant colors, (maybe flouro) with each flavor having its own distinct color.
4. Incorporate Key Ingredients on Packaging:
The front of each package should display the key ingredients for that specific flavor + an energy ball or not....
5. Fun Graphics of Ingredients:
Design graphics of the key ingredients that include fun, animated elements, such as faces, to create a playful and engaging look (similar to the attached graphics).
Looking to create standout packaging that aligns with my brand's fun and vibrant identity while allowing room for future growth and product line expansion.

```html
<!DOCTYPE html>
<html lang="en">
<head>
<meta charset="utf-8">
<title>Spark Bites – Flavour Range Packaging</title>
<link href="https://fonts.googleapis.com/css2?family=Baloo+2:wght@600;800&family=Lilita+One&display=swap" rel="stylesheet">
<style>
  :root {
    --bg: #f4f1ec;
    --white: #ffffff;
    --choc-pouch: #f0c400;
    --choc-pouch-deep: #e3b600;
    --choc-accent: #d3201e;
    --ginger-pouch: #e1067b;
    --ginger-pouch-deep: #cf046f;
    --ginger-accent: #f6d900;
    --oat-pouch: #2fc2e6;
    --oat-pouch-deep: #25b2d6;
    --oat-accent: #e2157a;
  }
  * { box-sizing: border-box; margin: 0; padding: 0; }
  html, body { width: 1200px; height: 1200px; overflow: hidden; }
  body { background: var(--bg); position: relative; font-family: "Baloo 2", sans-serif; }

  .range { position: absolute; inset: 0; }

  .pouch {
    position: absolute;
    top: 353px;
    width: 296px;
    height: 482px;
    border-radius: 14px 14px 2px 2px;
    background: var(--pouch);
    color: var(--white);
    text-align: center;
    overflow: hidden;
  }
  .pouch--chocolate { left: 49px;  --pouch: var(--choc-pouch);   --deep: var(--choc-pouch-deep);   --accent: var(--choc-accent); }
  .pouch--ginger    { left: 448px; --pouch: var(--ginger-pouch); --deep: var(--ginger-pouch-deep); --accent: var(--ginger-accent); }
  .pouch--oatmeal   { left: 859px; --pouch: var(--oat-pouch);    --deep: var(--oat-pouch-deep);    --accent: var(--oat-accent); }

  .pouch__seal {
    position: absolute; left: 0; right: 0; top: 50px; height: 14px;
    background: var(--deep);
  }

  .pouch__brand {
    position: absolute; top: 78px; left: 0; right: 0;
    display: flex; justify-content: center; align-items: flex-start; gap: 14px;
  }
  .product-name {
    font-family: "Lilita One", sans-serif;
    font-size: 34px; line-height: 1;
    color: var(--white);
    letter-spacing: 0.5px;
    width: 150px;
    text-align: center;
  }
  .maker-name {
    font-family: "Baloo 2", sans-serif;
    font-weight: 600;
    font-size: 10px; line-height: 1.15;
    color: var(--white);
    text-align: left;
    padding-top: 4px;
    text-transform: uppercase;
  }

  .pouch__tagline {
    position: absolute; top: 152px; left: 0; right: 0;
    font-size: 8.5px; font-weight: 800;
    color: var(--accent);
    letter-spacing: 0.3px;
  }

  .pouch__art {
    position: absolute; top: 185px; left: 40px; right: 40px; height: 165px;
    border-radius: 18px;
  }
  .pouch--chocolate .pouch__art { background: radial-gradient(ellipse at center, #a8552a 0%, #d39a3a 45%, var(--choc-pouch) 78%); }
  .pouch--ginger .pouch__art    { background: radial-gradient(ellipse at center, #e7b44a 0%, #b8305a 50%, var(--ginger-pouch) 80%); }
  .pouch--oatmeal .pouch__art   { background: radial-gradient(ellipse at center, #f3e2b8 0%, #c84a6a 40%, var(--oat-pouch) 80%); }

  .pouch__flavour {
    position: absolute; top: 368px; left: 0; right: 0;
    font-family: "Lilita One", sans-serif;
    font-size: 27px; line-height: 1.1;
    color: var(--accent);
  }

  .pouch__claims {
    position: absolute; top: 446px; left: 0; right: 0;
    font-size: 6.5px; font-weight: 800; letter-spacing: 0.4px;
    color: var(--white);
    text-transform: uppercase;
  }
</style>
</head>
<body>
<main class="range">

  <section class="pouch pouch--chocolate">
    <div class="pouch__seal"></div>
    <header class="pouch__brand">
      <div class="product-name">SPARK BITES</div>
      <div class="maker-name">Velvet Crumb<br>by Nora</div>
    </header>
    <p class="pouch__tagline">Fuel your day with a burst of Energy</p>
    <div class="pouch__art" role="img" aria-label="Illustration of a cheerful date, chocolate bar and cashew dancing together"></div>
    <h2 class="pouch__flavour">Dates, Cashew<br>&amp; Chocolate</h2>
    <p class="pouch__claims">No added sugar ¦ Vegan ¦ No preservatives</p>
  </section>

  <section class="pouch pouch--ginger">
    <div class="pouch__seal"></div>
    <header class="pouch__brand">
      <div class="product-name">SPARK BITES</div>
      <div class="maker-name">Velvet Crumb<br>by Nora</div>
    </header>
    <p class="pouch__tagline">Fuel your day with a burst of Energy</p>
    <div class="pouch__art" role="img" aria-label="Illustration of a jumping date with a ginger root and cashew holding hands among sparkles"></div>
    <h2 class="pouch__flavour">Dates, Cashew<br>&amp; Ginger</h2>
    <p class="pouch__claims">No added sugar ¦ Vegan ¦ No preservatives</p>
  </section>

  <section class="pouch pouch--oatmeal">
    <div class="pouch__seal"></div>
    <header class="pouch__brand">
      <div class="product-name">SPARK BITES</div>
      <div class="maker-name">Velvet Crumb<br>by Nora</div>
    </header>
    <p class="pouch__tagline">Fuel your day with a burst of Energy</p>
    <div class="pouch__art" role="img" aria-label="Illustration of a cranberry surfing on an oatmeal bowl beside a date relaxing on a beach towel under clouds"></div>
    <h2 class="pouch__flavour">Dates, Cranberries<br>&amp; Oatmeal</h2>
    <p class="pouch__claims">No added sugar ¦ Vegan ¦ No preservatives</p>
  </section>

</main>
</body>
</html>
```